Helix Anchor Works Website

Hello we are a screw piling business based in Sydney.
Screw piling is basically drilling steel into the ground with a excavator.

The website needs to have similar information as http://www.brightgroundworks.com.au/. It is basically the same business.

The business name is Helix Anchor Works.

Logo is attached.

Website needs to be wordpress ready.
With SEO.
Want to be able to edit in wordpress.

Target Market(s)

Business to Business and Normal

Industry/Entity Type

Construction

Coding

Coded - Design and coding required

Number of Pages Required

5+ page

Font styles to use
Serif
Sans Serif
Decorative

Requirements
Nice to have
• Information about screw piering.

```html
<!DOCTYPE html>
<html lang="en">
<head>
<meta charset="utf-8">
<title>Helix Anchor Works</title>
<link href="https://fonts.googleapis.com/css2?family=Roboto:ital,wght@0,300;0,400;0,500;0,700;1,400&display=swap" rel="stylesheet">
<style>
:root{
  --blue:#0a63d6;
  --blue-dark:#0750b3;
  --ink:#333;
  --text:#666;
  --muted:#999;
  --line:#e6e6e6;
  --footer:#262626;
  --star:#f0a30a;
  --white:#fff;
}
*{margin:0;padding:0;box-sizing:border-box}
html,body{width:717px;height:1200px;overflow:hidden;background:var(--white)}
body{font-family:'Roboto',sans-serif;color:var(--ink)}
.page{position:relative;width:717px;height:1200px;overflow:hidden}
.abs{position:absolute}

/* header */
.header{left:0;top:0;width:717px;height:58px;background:var(--white);border-top:2px solid var(--blue);box-shadow:0 1px 3px rgba(0,0,0,.08);z-index:2}
.brand{left:52px;top:19px;display:flex;align-items:center;gap:6px}
.brand-mark{width:14px;height:14px;background:var(--blue)}
.brand-name{font-weight:700;font-size:14px;color:var(--blue);letter-spacing:.2px;text-transform:uppercase}
.nav a{position:absolute;top:0;height:56px;line-height:56px;font-size:7.6px;color:var(--ink);text-decoration:none;text-transform:uppercase;letter-spacing:.2px}
.nav a.active{background:var(--blue);color:var(--white);text-align:center}

/* hero */
.hero{left:0;top:58px;width:717px;height:280px;background:linear-gradient(100deg,#2b2e33 0%,#3c3e42 45%,#4b3a30 75%,#3a3634 100%)}
.hero-text{left:0;width:717px;text-align:center;color:var(--white)}
.hero-kicker{top:135px;font-weight:300;font-size:18px;letter-spacing:.3px}
.hero-title{top:157px;font-weight:700;font-size:27px}
.hero-lead{top:199px;left:150px;width:417px;font-size:8.4px;line-height:16px}
.btn-outline{border:1px solid rgba(255,255,255,.85);color:var(--white);font-size:8px;font-weight:500;text-transform:uppercase;display:flex;align-items:center;justify-content:center}
.hero-btn{left:289px;top:243px;width:139px;height:29px}
.hero-arrow{top:184px;width:28px;height:28px;border:1.5px solid var(--white);border-radius:50%}

/* services */
.section-title{font-size:13px;font-weight:400;text-transform:uppercase;color:var(--ink)}
.pager{top:354px;display:flex;gap:1px}
.card{top:380px;width:192px;height:237px;background:var(--white);border:1px solid #eee;box-shadow:0 0 3px rgba(0,0,0,.08)}
.card-photo{position:absolute;left:7px;top:7px;width:178px;height:122px}
.card-title{position:absolute;left:9px;top:142px;font-size:9.6px;font-weight:500;color:var(--blue);text-transform:uppercase}
.card-text{position:absolute;left:9px;top:160px;width:176px;font-size:7.3px;line-height:14px;color:var(--text)}
.card-more{position:absolute;left:9px;top:212px;font-size:7.3px;color:var(--blue);text-transform:uppercase}

/* about band */
.about{left:0;top:644px;width:717px;height:184px;background:linear-gradient(90deg,var(--blue-dark),var(--blue) 50%,#1772e6);color:var(--white);text-align:center}
.about-title{position:absolute;left:0;top:25px;width:717px;font-size:15px;font-weight:500;text-transform:uppercase}
.about-sub{position:absolute;left:0;top:52px;width:717px;font-size:7.6px;text-transform:uppercase}
.about-text{position:absolute;left:138px;top:74px;width:441px;font-size:7.6px;line-height:16px}
.about-btn{position:absolute;left:307px;top:134px;width:103px;height:29px;font-size:8.4px}

/* gallery */
.tile{width:112px;height:73px}

/* testimonials */
.avatar{width:46px;height:46px;border-radius:50%;background:linear-gradient(135deg,#d9d2cc,#b9aca2)}
.quote-meta{font-size:7px;font-style:italic;color:var(--text)}
.quote-meta b{font-weight:400;color:var(--blue)}
.quote-text{font-size:7.3px;font-style:italic;color:var(--text);line-height:14px;width:170px}
.stars{font-size:7px;color:var(--star);letter-spacing:.5px}
.rule{height:1px;background:var(--line)}

/* partners */
.partner{top:1074px;font-size:15px;font-weight:500;color:#b3b3b3;display:flex;align-items:center;gap:5px}
.partner i{display:block;width:14px;height:14px;background:#c4c4c4}

/* footer */
.footer{left:0;top:1116px;width:717px;height:84px;background:var(--footer)}
.foot-nav{left:0;top:19px;width:717px;display:flex;justify-content:center;font-size:7.2px;color:var(--white);text-transform:uppercase}
.foot-nav span{padding:0 14px}
.foot-nav em{font-style:normal}
.foot-rule{left:51px;top:42px;width:614px;height:1px;background:#3b3b3b}
.copy{left:52px;top:59px;font-size:7.2px;color:var(--white)}
.social{top:51px;width:20px;height:20px;border:1.3px solid var(--white);border-radius:50%}
</style>
</head>
<body>
<div class="page">

  <header class="abs header">
    <div class="abs brand"><span class="brand-mark"></span><span class="brand-name">Helix Anchor Works</span></div>
    <nav class="nav">
      <a class="active" style="left:249px;width:52px">Home</a>
      <a style="left:315px">About Us</a>
      <a style="left:380px">Services</a>
      <a style="left:444px">Products</a>
      <a style="left:512px">Benefits</a>
      <a style="left:575px">FAQ</a>
      <a style="left:618px">Contact Us</a>
    </nav>
  </header>

  <section class="abs hero" role="img" aria-label="Excavator working on a rocky construction site"></section>
  <div class="abs hero-text hero-kicker">WELCOME TO</div>
  <h1 class="abs hero-text hero-title">HELIX ANCHOR WORKS</h1>
  <p class="abs hero-lead hero-text">It is a long established fact that a reader will be distracted by the readable content of a page when looking at its normal distribution of letters, as opposed to using making it look like readable English.</p>
  <div class="abs btn-outline hero-btn">Click here for more info</div>
  <svg class="abs hero-arrow" style="left:18px" viewBox="0 0 28 28"><path d="M16 9l-5 5 5 5" fill="none" stroke="#fff" stroke-width="2"/></svg>
  <svg class="abs hero-arrow" style="left:670px" viewBox="0 0 28 28"><path d="M12 9l5 5-5 5" fill="none" stroke="#fff" stroke-width="2"/></svg>

  <h2 class="abs section-title" style="left:51px;top:352px">Our Services</h2>
  <div class="abs pager" style="left:640px">
    <svg width="12" height="11" viewBox="0 0 12 11"><rect width="12" height="11" fill="#777"/><path d="M7 3L4.5 5.5 7 8" fill="none" stroke="#fff" stroke-width="1.2"/></svg>
    <svg width="12" height="11" viewBox="0 0 12 11"><rect width="12" height="11" fill="#777"/><path d="M5 3l2.5 2.5L5 8" fill="none" stroke="#fff" stroke-width="1.2"/></svg>
  </div>

  <article class="abs card" style="left:51px">
    <div class="card-photo" role="img" aria-label="Screws, bolts and tools on a workbench" style="background:linear-gradient(135deg,#5a3a2a,#8a8078 55%,#3a2a22)"></div>
    <h3 class="card-title">Screw Piling</h3>
    <p class="card-text">It is a long established fact that a reader will be distracted by the readable content of a page when looking at its layout.....</p>
    <a class="card-more">[ Read More ]</a>
  </article>
  <article class="abs card" style="left:262px">
    <div class="card-photo" role="img" aria-label="Drill press cutting into steel" style="background:linear-gradient(135deg,#4a4a4a,#9a9a98 55%,#6a6a68)"></div>
    <h3 class="card-title">Drilling Steel</h3>
    <p class="card-text">It is a long established fact that a reader will be distracted by the readable content of a page when looking at its layout.....</p>
    <a class="card-more">[ Read More ]</a>
  </article>
  <article class="abs card" style="left:472px">
    <div class="card-photo" role="img" aria-label="Excavator on a gravel site" style="background:linear-gradient(180deg,#6d7a86,#8e9196 50%,#a39c94)"></div>
    <h3 class="card-title">Excavator</h3>
    <p class="card-text">It is a long established fact that a reader will be distracted by the readable content of a page when looking at its layout.....</p>
    <a class="card-more">[ Read More ]</a>
  </article>

  <section class="abs about">
    <h2 class="about-title">About Helix Anchor Works</h2>
    <p class="about-sub">It is a long established fact that a reader will be distracted by the readable content</p>
    <p class="about-text">It is a long established fact that a reader will be distracted by the readable content of a page when looking at its layout. The point of using Lorem Ipsum is that it has a more-or-less normal distribution of letters, as opposed to using Content here content here making it look like readable English.</p>
    <div class="btn-outline about-btn">Read More Info</div>
  </section>

  <h2 class="abs section-title" style="left:50px;top:848px">Photo Gallery</h2>
  <div class="abs tile" style="left:51px;top:877px;background:linear-gradient(135deg,#3a3532,#6e6258)" role="img" aria-label="Welder working on steel"></div>
  <div class="abs tile" style="left:171px;top:877px;background:linear-gradient(135deg,#6d7a6a,#3e6a6a)" role="img" aria-label="Drill press in a workshop"></div>
  <div class="abs tile" style="left:291px;top:877px;background:linear-gradient(135deg,#c9b26a,#8c8c8c)" role="img" aria-label="Worker with jackhammer on site"></div>
  <div class="abs tile" style="left:51px;top:960px;background:linear-gradient(135deg,#5c4a3e,#9c8e84)" role="img" aria-label="Hands cutting metal"></div>
  <div class="abs tile" style="left:171px;top:960px;background:linear-gradient(135deg,#b56a3e,#d89a70)" role="img" aria-label="Drill bit boring into wood"></div>
  <div class="abs tile" style="left:291px;top:960px;background:linear-gradient(135deg,#8a98a6,#6e6a68)" role="img" aria-label="Core drill on a concrete slab"></div>

  <h2 class="abs section-title" style="left:431px;top:850px">Our Testimonials</h2>
  <svg class="abs" style="left:675px;top:851px" width="18" height="8" viewBox="0 0 18 8"><path d="M4 1L1 4l3 3M14 1l3 3-3 3" fill="none" stroke="#bbb" stroke-width="1"/></svg>

  <div class="abs avatar" style="left:432px;top:878px" role="img" aria-label="Client portrait"></div>
  <p class="abs quote-meta" style="left:493px;top:878px">By <b>Dale Moreno</b> on 14 August 2015</p>
  <p class="abs quote-text" style="left:493px;top:893px">It is a long established fact that a reader will be content of a page when looking at its layout</p>
  <div class="abs stars" style="left:493px;top:924px">★★★★☆</div>
  <div class="abs rule" style="left:432px;top:951px;width:234px"></div>

  <div class="abs avatar" style="left:432px;top:967px" role="img" aria-label="Client portrait"></div>
  <p class="abs quote-meta" style="left:495px;top:967px">By <b>Dale Moreno</b> on 14 August 2015</p>
  <p class="abs quote-text" style="left:495px;top:982px">It is a long established fact that a reader will be content of a page when looking at its layout</p>
  <div class="abs stars" style="left:495px;top:1013px">★★★★☆</div>

  <div class="abs rule" style="left:51px;top:1058px;width:614px"></div>
  <svg class="abs" style="left:40px;top:1078px" width="8" height="12" viewBox="0 0 8 12"><path d="M6 1L1 6l5 5" fill="none" stroke="#bbb" stroke-width="1.2"/></svg>
  <div class="abs partner" style="left:66px"><i style="border-radius:50%"></i>Soundvale</div>
  <div class="abs partner" style="left:166px"><i></i>Gridworks</div>
  <div class="abs partner" style="left:276px">Snapleaf</div>
  <div class="abs partner" style="left:373px">Frameyard</div>
  <div class="abs partner" style="left:484px"><i></i>Tilebase</div>
  <div class="abs partner" style="left:583px">Snapleaf</div>
  <svg class="abs" style="left:669px;top:1078px" width="8" height="12" viewBox="0 0 8 12"><path d="M2 1l5 5-5 5" fill="none" stroke="#bbb" stroke-width="1.2"/></svg>

  <footer class="abs footer">
    <div class="abs foot-nav">
      <span>Home</span><em>|</em><span>About Us</span><em>|</em><span>Services</span><em>|</em><span>Products</span><em>|</em><span>Benefits</span><em>|</em><span>FAQ</span><em>|</em><span>Contact Us</span>
    </div>
    <div class="abs foot-rule"></div>
    <p class="abs copy">©Copy Right 2015 Helix Anchor Works.All Rights Reserved.</p>
    <span class="abs social" style="left:562px"></span>
    <span class="abs social" style="left:590px"></span>
    <span class="abs social" style="left:618px"></span>
    <span class="abs social" style="left:646px"></span>
  </footer>

</div>
</body>
</html>
```